Young Balance Support Network

We need a poster explaining that some children live with a disability called Vestibular Disorder. Feel free to ask question. We want you to respect our color code, same as our logo.

Here is our website : http://www.ybsnetwork.org/

We need to sensibilise people about this disability for children.

Industry/Entity Type

Charity

Font styles to use
Serif

Requirements
Must have
• 1. our logo (with all our details) + one of the photo of Marek
• 2. design showing a child with a dizziness for exemple
• 3. a title saying : Aidez-nous à changer la vie des enfants vivant avec un problème vestibulaire
• 4.include the text attached (information flyer YBSN)
• Poster size : 24"X 36"
Should not have
• wheel chair

```html
<!DOCTYPE html>
<html lang="fr">
<head>
<meta charset="utf-8">
<title>Aidez-nous à changer la vie des enfants – Young Balance Support Network</title>
<link rel="stylesheet" href="https://fonts.googleapis.com/css2?family=Lato:wght@300;400;700;900&display=swap">
<style>
  :root {
    --sky: #4BBFEF;
    --orange: #F7A400;
    --sun: #FFC81A;
    --lime: #C5D62A;
    --heading-blue: #1A8BC8;
    --navy: #1F3A5A;
    --ink: #1E1E1E;
    --footer-ink: #26331A;
    --stage: #636363;
    --white: #FFFFFF;
  }
  * { box-sizing: border-box; margin: 0; padding: 0; }
  html, body { width: 1200px; height: 1200px; overflow: hidden; }
  body {
    background: var(--stage);
    font-family: "Lato", Arial, sans-serif;
    color: var(--ink);
  }
  .poster {
    position: absolute;
    left: 200px; top: 0;
    width: 800px; height: 1200px;
    overflow: hidden;
    background: var(--white);
  }
  .poster-bg { position: absolute; inset: 0; width: 800px; height: 1200px; }

  .title {
    position: absolute;
    left: 28px; top: 74px;
    font-weight: 300;
    font-size: 30px;
    line-height: 37px;
    color: var(--white);
    text-transform: uppercase;
    letter-spacing: 0.2px;
  }
  .title .accent { color: var(--orange); }

  .column { position: absolute; width: 330px; }
  .column-left { left: 44px; top: 604px; }
  .column-right { left: 408px; top: 598px; }

  .qa { margin-bottom: 22px; }
  .qa h2 {
    position: relative;
    padding-left: 22px;
    font-size: 14px;
    font-weight: 700;
    line-height: 18px;
    color: var(--heading-blue);
    text-transform: uppercase;
    letter-spacing: -0.2px;
  }
  .tick {
    position: absolute; left: 0; top: 2px;
    width: 15px; height: 15px;
  }
  .qa p {
    padding-left: 22px;
    font-size: 13.6px;
    line-height: 18px;
    text-align: justify;
    margin-top: 10px;
  }
  .qa h2 + p.tight { margin-top: 0; }

  .logo-block {
    position: absolute;
    left: 466px; top: 932px;
    width: 240px;
  }
  .logo-name {
    font-weight: 900;
    font-size: 14.5px;
    line-height: 15px;
    letter-spacing: 1.4px;
    color: var(--navy);
    text-transform: uppercase;
    width: 140px;
  }
  .logo-mark {
    position: absolute; left: 160px; top: 2px;
    width: 56px; height: 56px; border-radius: 50%;
    background: var(--sky);
  }
  .logo-details { margin-top: 12px; font-size: 7.5px; line-height: 16px; letter-spacing: 0.4px; }
  .logo-details .web { color: var(--heading-blue); }
  .logo-details .mail { color: var(--orange); }
  .logo-details .ccp { color: var(--heading-blue); display: flex; align-items: center; gap: 14px; margin-top: 4px; }
  .dot { width: 13px; height: 13px; background: var(--navy); display: inline-block; border-radius: 2px; }
  .dot.light { background: var(--sky); border-radius: 50%; }

  .footer {
    position: absolute;
    left: 0; top: 1154px; width: 800px; height: 26px;
    font-size: 18px; font-weight: 700; color: var(--footer-ink);
  }
  .footer-item { position: absolute; top: 0; display: flex; align-items: center; gap: 14px; }
  .footer-mail { left: 72px; }
  .footer-web { left: 372px; }
  .footer-social { left: 682px; gap: 12px; top: 4px; }
  .footer-social .dot { width: 20px; height: 20px; }
</style>
</head>
<body>
<main class="poster">
  <svg class="poster-bg" viewBox="0 0 800 1200" aria-hidden="false">
    <defs>
      <linearGradient id="sunGradient" x1="0" y1="0" x2="1" y2="1">
        <stop offset="0" stop-color="#F79A00"/>
        <stop offset="1" stop-color="#FFCC1F"/>
      </linearGradient>
      <linearGradient id="photoTone" x1="0" y1="0" x2="0" y2="1">
        <stop offset="0" stop-color="#C9A27E"/>
        <stop offset="0.5" stop-color="#DDB69A"/>
        <stop offset="1" stop-color="#C79B80"/>
      </linearGradient>
    </defs>
    <rect class="sky-field" x="0" y="0" width="800" height="620" fill="var(--sky)"/>
    <path class="sun-field" d="M470 0 H800 V570 C700 610 560 650 360 610 C450 520 420 420 400 300 C385 180 405 60 470 0Z" fill="url(#sunGradient)"/>
    <path class="hero-photo" role="img" aria-label="Photo d'un jeune enfant aux yeux plissés, les mains pressées sur les oreilles"
      d="M525 0 H755 C795 60 800 260 800 420 V530 C700 540 560 520 440 480 C300 440 150 425 155 385 C160 330 280 310 405 305 C410 200 450 60 525 0Z"
      fill="url(#photoTone)"/>
    <path class="wave-band" d="M0 455 C50 545 150 580 300 565 C440 550 520 490 600 485 C700 480 760 520 800 560 V1200 H0Z" fill="var(--lime)"/>
    <path class="wave-white" d="M0 470 C60 565 160 596 300 582 C440 568 520 506 600 502 C700 498 760 545 800 590 V1200 H0Z" fill="var(--white)"/>
    <path class="footer-wave" d="M0 940 C30 1080 180 1150 370 1140 C550 1130 690 1080 800 1058 V1200 H0Z" fill="var(--lime)"/>
  </svg>

  <h1 class="title">Aidez-nous à changer<br>la vie des enfants<br>vivant avec un<br>problème<br><span class="accent">vestibulaire</span></h1>

  <section class="column column-left">
    <article class="qa">
      <h2><svg class="tick" viewBox="0 0 16 16"><circle cx="8" cy="8" r="8" fill="var(--orange)"/><path d="M4.5 8.2 L7 10.6 L11.6 5.6" fill="none" stroke="#fff" stroke-width="1.8" stroke-linecap="round" stroke-linejoin="round"/></svg>Qu'est-ce que le vestibule ?</h2>
      <p class="tight">C'est un organe sensoriel, pilier de votre équilibre, véritable 6ème sens situé dans l'oreille interne.</p>
    </article>
    <article class="qa">
      <h2><svg class="tick" viewBox="0 0 16 16"><circle cx="8" cy="8" r="8" fill="var(--orange)"/><path d="M4.5 8.2 L7 10.6 L11.6 5.6" fill="none" stroke="#fff" stroke-width="1.8" stroke-linecap="round" stroke-linejoin="round"/></svg>Quelles en sont les conséquences<br>pour l'enfant ?</h2>
      <p>Le développement moteur de l'enfant est retardé car il doit trouver des solutions afin de construire son équilibre, stabiliser son regard et son corps.</p>
      <p>Certains apprentissages sont de véritables obstacles pour l'enfant : se représenter son propre corps, se situer dans l'espace qui l'entoure, interagir avec les autres, communiquer, écrire, lire, manger, boire, marcher. Chacune de ces actions necessitent des efforts considérables pour se concentrer quelques secondes ou minutes.</p>
      <p>Quand l'enfant réussit à effectuer l'une de ces actions, son comportement peut sembler déroutant et bien trop souvent mal interprété par le grand public.</p>
    </article>
  </section>

  <section class="column column-right">
    <article class="qa">
      <h2><svg class="tick" viewBox="0 0 16 16"><circle cx="8" cy="8" r="8" fill="var(--orange)"/><path d="M4.5 8.2 L7 10.6 L11.6 5.6" fill="none" stroke="#fff" stroke-width="1.8" stroke-linecap="round" stroke-linejoin="round"/></svg>Qu'est ce qu'une aréflexie vestibulaire ?</h2>
      <p>C'est l'absence complète de toute information vestibulaire. L'enfant a ainsi l impression que tout vacille autour de lui, jour et nuit.</p>
    </article>
    <article class="qa">
      <h2><svg class="tick" viewBox="0 0 16 16"><circle cx="8" cy="8" r="8" fill="var(--orange)"/><path d="M4.5 8.2 L7 10.6 L11.6 5.6" fill="none" stroke="#fff" stroke-width="1.8" stroke-linecap="round" stroke-linejoin="round"/></svg>Quel est le but de notre association ?</h2>
      <p>Notre association a pour but de promouvoir les troubles vestibulaires chez l'enfant, ses conséquences sur sa santé ainsi que celui de son entourage et de soutenir ces enfants et leurs parents en leur offrant un espace de parole et des solutions concrètes pour soulager leur quotidien. Notre association a également pour but de financer et promouvoir toute action de recherche scientifique visant à aider les enfants ayant un trouble vestibulaire.</p>
    </article>
  </section>

  <aside class="logo-block">
    <div class="logo-name">Young Balance Support Network</div>
    <span class="logo-mark"></span>
    <div class="logo-details">
      <div class="web">WWW.YBSNETWORK.ORG</div>
      <div class="mail">INFO@YBSNETWORK.ORG</div>
      <div class="ccp">CCP: 12-345678-9 <span class="dot"></span><span class="dot light"></span></div>
    </div>
  </aside>

  <footer class="footer">
    <div class="footer-item footer-mail">
      <svg width="20" height="14" viewBox="0 0 20 14"><rect x="1" y="1" width="18" height="12" fill="none" stroke="var(--footer-ink)" stroke-width="1.8"/><path d="M1 1 L10 8 L19 1" fill="none" stroke="var(--footer-ink)" stroke-width="1.8"/></svg>
      <span>info@ybsnetwork.org</span>
    </div>
    <div class="footer-item footer-web">
      <svg width="20" height="20" viewBox="0 0 20 20"><circle cx="10" cy="10" r="8.5" fill="none" stroke="var(--footer-ink)" stroke-width="1.6"/><ellipse cx="10" cy="10" rx="3.6" ry="8.5" fill="none" stroke="var(--footer-ink)" stroke-width="1.4"/><path d="M1.5 10 H18.5 M3 5.5 H17 M3 14.5 H17" stroke="var(--footer-ink)" stroke-width="1.3"/></svg>
      <span>www.ybsnetwork.org</span>
    </div>
    <div class="footer-item footer-social">
      <span class="dot"></span><span class="dot light"></span>
    </div>
  </footer>
</main>
</body>
</html>
```